Song Cover Art. Song Tittle Lift The Floor

I would like a design for my songs. I'm a producer and i prouder EDM music such as Big Room House / Electro House music. Currently i have a new songs tittle name Lift The Floor and i need a cover art for my songs. I'm not sure what design i have in mind right now and i would like someone to create it for me. My DJ name is DJ Vex.
Reason: Hey, i will give sometimes for you guys to create the design for me. Please do zorvix edm cover art or brenlow - lift the floor.
Target Market(s)
Electronic Dance Music Lovers
Industry/Entity Type
House
Look and feel
Each slider illustrates characteristics of the customer's brand and the style your logo design should communicate.

```html
<!DOCTYPE html>
<html lang="en">
<head>
<meta charset="utf-8">
<title>DJ Vex – Lift The Floor</title>
<link rel="stylesheet" href="https://fonts.googleapis.com/css2?family=Open+Sans:wght@700&display=swap">
<style>
  :root {
    --ink-navy: #1c0a4a;
    --hot-red: #ff1e3c;
    --magenta: #c8176a;
    --deep-violet: #3a0c5c;
    --paper: #ffffff;
  }
  html, body {
    margin: 0;
    padding: 0;
    width: 1200px;
    height: 1200px;
    overflow: hidden;
    background: var(--ink-navy);
  }
  .cover {
    position: relative;
    width: 1200px;
    height: 1200px;
    overflow: hidden;
  }
  .cover-artwork {
    position: absolute;
    inset: 0;
    background:
      radial-gradient(ellipse 45% 40% at 30% 30%, var(--hot-red) 0%, transparent 70%),
      radial-gradient(ellipse 40% 35% at 65% 55%, var(--hot-red) 0%, transparent 75%),
      radial-gradient(ellipse 35% 30% at 20% 80%, var(--magenta) 0%, transparent 75%),
      radial-gradient(ellipse 30% 25% at 85% 20%, var(--magenta) 0%, transparent 75%),
      linear-gradient(135deg, var(--deep-violet), var(--ink-navy) 60%, var(--deep-violet));
  }
  .artist-name {
    position: absolute;
    left: 44px;
    top: 45px;
    margin: 0;
    font-family: "Open Sans", Arial, sans-serif;
    font-weight: 700;
    font-size: 84px;
    line-height: 1;
    color: var(--paper);
    white-space: nowrap;
  }
  .song-title {
    position: absolute;
    left: 806px;
    bottom: 50px;
    margin: 0;
    font-family: "Open Sans", Arial, sans-serif;
    font-weight: 700;
    font-size: 112px;
    line-height: 92px;
    letter-spacing: -3px;
    color: var(--paper);
    text-transform: uppercase;
    white-space: nowrap;
  }
  .song-title span { display: block; }
</style>
</head>
<body>
  <main class="cover">
    <div class="cover-artwork" role="img" aria-label="Abstract illustration of a stylised figure in profile over swirling red, magenta and navy liquid patterns"></div>
    <p class="artist-name">DJ Vex</p>
    <h1 class="song-title"><span>Lift</span><span>The</span><span>Floor</span></h1>
  </main>
</body>
</html>
```